Crestwell Advisory Services

I'm looking to create a flyer for my business to provide a consultant service. I will be providing the following below
Launch Your Business Today for only $150
(state fee not included)
Business Formation includes:
*Limited liability Corporation (LLC)
*Halvers and Quint Number
*FEIN
*Operation Agreement for partnership LLCs (For 2 or more member(s)
*Commercial Activity license (If needed for your Business )
*Same -day turnaround service with documents
Schedule your Appointment today
Call or text:318-472-6051
Email:MoralesCapitalCircle@fernmail.net
Target Market(s)
I want the flyer to attract people who wants to start a business but doesn’t know where to start. I want the flyer to stand out form the other consultant businesses.
Industry/Entity Type
Consultant
Requirements
Must have
- The State fee not included should be in small print
Highlight the price or service
Highlight the phrase "launch you business today"
Nice to have
- Different samples of colors, a variety
Should not have
- should not be all one color

```html
<!DOCTYPE html>
<html lang="en">
<head>
<meta charset="utf-8">
<title>Crestwell Advisory Services – Business Formation Flyer</title>
<link href="https://fonts.googleapis.com/css2?family=Bebas+Neue&family=Cinzel:wght@400&family=Lato:wght@400;700&display=swap" rel="stylesheet">
<style>
  :root {
    --navy: #13264f;
    --red: #b3202a;
    --white: #ffffff;
    --paper: #f1f2f4;
    --ink: #1b1f2a;
    --stage: #e4e4e6;
    --photo-a: #c9c3bb;
    --photo-b: #5d5f6b;
  }
  * { margin: 0; padding: 0; box-sizing: border-box; }
  html, body { width: 1200px; height: 848px; overflow: hidden; background: var(--stage); }
  .flyer {
    position: absolute; left: 295px; top: 28px;
    width: 610px; height: 792px;
    background: var(--paper);
    font-family: "Lato", Arial, sans-serif;
    color: var(--ink);
    overflow: hidden;
    box-shadow: 0 6px 18px rgba(0,0,0,.18);
  }
  .flyer > * { position: absolute; }
  .top-white { left: 0; top: 0; width: 610px; height: 423px; background: var(--white); }
  .shapes, .hero-photo { left: 0; top: 0; }
  .brand {
    left: 16px; top: 34px; width: 220px;
    font-family: "Cinzel", Georgia, serif; font-size: 21px; line-height: 29px;
    color: var(--navy); text-align: center; letter-spacing: .3px;
  }
  .headline {
    left: 28px; top: 192px;
    font-family: "Bebas Neue", Impact, sans-serif; color: var(--white);
    font-size: 42px; line-height: 46px; letter-spacing: .5px;
  }
  .price {
    left: 17px; top: 290px; width: 236px; height: 37px;
    background: var(--red); border-radius: 3px;
    font-family: "Bebas Neue", Impact, sans-serif; color: var(--white);
    font-size: 41px; line-height: 40px; padding-left: 11px; letter-spacing: .5px;
  }
  .state-fee { left: 28px; top: 335px; font-size: 13px; color: #dfe3ee; }
  .prompt-band {
    left: 0; top: 423px; width: 610px; height: 58px; background: var(--red);
    color: var(--white); font-weight: 700; font-size: 15.5px;
  }
  .prompt-band span { position: absolute; top: 20px; }
  .prompt-band .ask { left: 25px; }
  .prompt-band .firm { left: 328px; }
  .services-card {
    left: 17px; top: 515px; width: 580px; height: 198px;
    background: var(--white); border-radius: 8px;
  }
  .services-tab {
    left: 9px; top: 503px; width: 296px; height: 26px;
    background: var(--navy); color: var(--white);
    font-weight: 700; font-size: 13.5px; line-height: 26px; padding-left: 16px;
    clip-path: polygon(0 0, 96% 0, 100% 100%, 0 100%);
  }
  .service { display: flex; align-items: center; gap: 6px; font-size: 13px; line-height: 14px; }
  .service svg { flex: none; }
  .footer-navy { left: 0; top: 733px; }
  .footer-red { left: 270px; top: 753px; width: 340px; height: 23px; background: var(--red); }
  .footer-base { left: 0; top: 776px; width: 610px; height: 16px; background: var(--navy); }
  .schedule { left: 16px; top: 746px; color: var(--white); font-size: 12px; font-weight: 700; line-height: 19px; }
  .schedule .call { font-weight: 400; display: flex; align-items: center; gap: 5px; }
  .schedule .call b { font-weight: 700; }
  .email { left: 348px; top: 757px; color: var(--white); font-size: 11.5px; display: flex; align-items: center; gap: 6px; }
</style>
</head>
<body>
<div class="flyer">
  <div class="top-white"></div>

  <svg class="hero-photo" width="610" height="792" role="img" aria-label="Photo of two business people in conversation over coffee in a bright office">
    <defs>
      <linearGradient id="photoTone" x1="0" y1="0" x2="1" y2="1">
        <stop offset="0" stop-color="var(--photo-a)"/>
        <stop offset="1" stop-color="var(--photo-b)"/>
      </linearGradient>
    </defs>
    <polygon points="363,34 610,34 610,423 303,423 341,348 240,173" fill="url(#photoTone)"/>
  </svg>

  <svg class="shapes" width="610" height="792" aria-hidden="true">
    <polygon points="0,116 200,116 341,348 303,423 0,423" fill="var(--navy)"/>
  </svg>

  <div class="brand">MORALES<br>CAPITAL CIRCLE</div>

  <h1 class="headline">LAUNCH YOUR<br>BUSINESS TODAY</h1>
  <div class="price">FOR ONLY $150</div>
  <p class="state-fee">(state fee not included)</p>

  <div class="prompt-band">
    <span class="ask">DON’T KNOW WHERE TO START?</span>
    <span class="firm">CRESTWELL ADVISORY SERVICES</span>
  </div>

  <div class="services-card"></div>
  <div class="services-tab">BUSINESS FORMATION INCLUDES:</div>

  <div class="service" style="left:24px;top:549px;">
    <svg width="48" height="44" viewBox="0 0 48 44" aria-hidden="true"><polygon points="12,2 36,2 46,22 36,42 12,42 2,22" fill="none" stroke="var(--navy)" stroke-width="1.5"/><rect x="16" y="18" width="16" height="14" fill="var(--red)"/><rect x="19" y="13" width="10" height="5" fill="var(--navy)"/></svg>
    <span>Limited liability Corporation (LLC)</span>
  </div>
  <div class="service" style="left:24px;top:597px;">
    <svg width="48" height="44" viewBox="0 0 48 44" aria-hidden="true"><polygon points="12,2 36,2 46,22 36,42 12,42 2,22" fill="none" stroke="var(--navy)" stroke-width="1.5"/><circle cx="24" cy="21" r="6" fill="var(--red)"/><rect x="22" y="27" width="4" height="5" fill="var(--navy)"/></svg>
    <span>Halvers and Quint Number</span>
  </div>
  <div class="service" style="left:24px;top:645px;">
    <svg width="48" height="44" viewBox="0 0 48 44" aria-hidden="true"><polygon points="12,2 36,2 46,22 36,42 12,42 2,22" fill="none" stroke="var(--navy)" stroke-width="1.5"/><rect x="21" y="12" width="12" height="16" fill="var(--red)"/><circle cx="20" cy="26" r="5" fill="none" stroke="var(--navy)" stroke-width="2"/><line x1="16" y1="30" x2="13" y2="33" stroke="var(--navy)" stroke-width="2"/></svg>
    <span>FEIN</span>
  </div>

  <div class="service" style="left:301px;top:549px;">
    <svg width="48" height="44" viewBox="0 0 48 44" aria-hidden="true"><polygon points="12,2 36,2 46,22 36,42 12,42 2,22" fill="none" stroke="var(--navy)" stroke-width="1.5"/><circle cx="17" cy="18" r="3" fill="var(--red)"/><circle cx="31" cy="18" r="3" fill="var(--red)"/><circle cx="24" cy="20" r="3.5" fill="var(--navy)"/><rect x="14" y="24" width="20" height="6" rx="3" fill="var(--navy)"/></svg>
    <span>Operation Agreement for partnership<br>LLCs (For 2 or more member(s)</span>
  </div>
  <div class="service" style="left:301px;top:597px;">
    <svg width="48" height="44" viewBox="0 0 48 44" aria-hidden="true"><polygon points="12,2 36,2 46,22 36,42 12,42 2,22" fill="none" stroke="var(--navy)" stroke-width="1.5"/><rect x="16" y="11" width="15" height="20" fill="none" stroke="var(--red)" stroke-width="2"/><line x1="19" y1="17" x2="28" y2="17" stroke="var(--navy)" stroke-width="1.5"/><line x1="19" y1="21" x2="28" y2="21" stroke="var(--navy)" stroke-width="1.5"/><line x1="26" y1="31" x2="33" y2="22" stroke="var(--navy)" stroke-width="2"/></svg>
    <span>Commercial Activity license<br>(If needed for your Business )</span>
  </div>
  <div class="service" style="left:301px;top:645px;">
    <svg width="48" height="44" viewBox="0 0 48 44" aria-hidden="true"><polygon points="12,2 36,2 46,22 36,42 12,42 2,22" fill="none" stroke="var(--navy)" stroke-width="1.5"/><path d="M32 22 A8 8 0 1 1 24 14" fill="none" stroke="var(--red)" stroke-width="2"/><polyline points="24,17 24,22 28,25" fill="none" stroke="var(--navy)" stroke-width="2"/></svg>
    <span>Same -day turnaround service<br>with documents</span>
  </div>

  <svg class="footer-navy" width="290" height="59" aria-hidden="true">
    <polygon points="0,0 268,0 284,43 284,59 0,59" fill="var(--navy)"/>
  </svg>
  <div class="footer-red"></div>
  <div class="footer-base"></div>

  <div class="schedule">
    SCHEDULE YOUR APPOINTMENT TODAY
    <div class="call">Call or text:
      <svg width="11" height="13" viewBox="0 0 11 13" aria-hidden="true"><rect x="1.5" y="0.8" width="8" height="11.4" rx="1.5" fill="none" stroke="var(--white)" stroke-width="1.4"/><line x1="4.5" y1="10" x2="6.5" y2="10" stroke="var(--white)" stroke-width="1.2"/></svg>
      <b>318-472-6051</b>
    </div>
  </div>
  <div class="email">
    <svg width="10" height="10" viewBox="0 0 10 10" aria-hidden="true"><circle cx="5" cy="5" r="5" fill="var(--white)"/><rect x="2.4" y="3.2" width="5.2" height="3.6" fill="var(--red)"/></svg>
    MoralesCapitalCircle@fernmail.net
  </div>
</div>
</body>
</html>
```